Logo, Business Card and LetterHead

Im am looking for someone to design for me Logo of my company as well as the Business Card and LetterHead

My Company is called PT. Bumi Sentosa Abadi and I do export import business.

Logo is supposed to somehow show to clients link with international trade, world or Indonesia where company is located

Industry/Entity Type

Business

Logo Text

PT. Bumi Sentosa Abadi

Logo styles of interest
Pictorial/Combination Logo
Wordmark Logo

```html
<!DOCTYPE html>
<html lang="en">
<head>
<meta charset="utf-8">
<title>PT. Bumi Sentosa Abadi — Logo, Letterhead and Business Card</title>
<link rel="stylesheet" href="https://fonts.googleapis.com/css2?family=Roboto:wght@400;500;700&display=swap">
<style>
  :root {
    --page-bg: #ececec;
    --panel: #ffffff;
    --band: #3b3f46;
    --blue: #1f4f84;
    --blue-dark: #173d68;
    --brown: #6b4121;
    --brown-dark: #4f2f17;
    --ink: #222222;
    --frame: #d3d3d3;
    --muted: #8a8a8a;
  }
  * { box-sizing: border-box; margin: 0; padding: 0; }
  html, body { width: 1200px; height: 2346px; overflow: hidden; }
  body {
    background: var(--page-bg);
    font-family: "Roboto", Arial, sans-serif;
    color: var(--ink);
    position: relative;
  }
  .panel {
    position: absolute;
    left: 52px;
    width: 1096px;
    background: var(--panel);
  }
  .panel--logo {
    top: 70px; height: 640px;
    display: flex; align-items: center; justify-content: center;
  }
  .panel--letterheads { top: 864px; height: 676px; box-shadow: 0 14px 18px -12px rgba(0,0,0,.25); }
  .panel--cards { top: 1580px; height: 680px; box-shadow: 0 14px 18px -12px rgba(0,0,0,.25); }

  .brand-band {
    position: absolute; left: 52px; top: 744px; width: 1096px; height: 120px;
    background: var(--band);
    display: flex; align-items: center; justify-content: center;
  }

  /* wordmark */
  .wordmark { display: flex; align-items: center; }
  .wordmark__dot { border-radius: 50%; flex: none; }
  .wordmark__name { font-weight: 700; white-space: nowrap; line-height: 1; }

  .wordmark--hero { gap: 30px; margin-top: 4px; }
  .wordmark--hero .wordmark__dot { width: 190px; height: 190px; background: var(--brown); }
  .wordmark--hero .wordmark__name { font-size: 46px; color: var(--blue); }

  .wordmark--band { gap: 14px; }
  .wordmark--band .wordmark__dot { width: 48px; height: 48px; border: 5px solid #fff; }
  .wordmark--band .wordmark__name { font-size: 24px; color: #fff; }

  .wordmark--small { gap: 6px; }
  .wordmark--small .wordmark__dot { width: 20px; height: 20px; background: var(--brown); }
  .wordmark--small .wordmark__name { font-size: 10px; color: var(--blue); }

  .wordmark--card-back { gap: 10px; }
  .wordmark--card-back .wordmark__dot { width: 22px; height: 22px; background: #fff; }
  .wordmark--card-back .wordmark__name { font-size: 18px; color: #fff; }

  /* letterheads */
  .letterhead {
    position: absolute; top: 56px; width: 446px; height: 570px;
    background: var(--frame); padding: 14px 15px;
  }
  .letterhead--left { left: 72px; }
  .letterhead--right { left: 618px; width: 440px; }
  .letterhead__paper { position: relative; width: 100%; height: 100%; background: #fff; overflow: hidden; }
  .letterhead__art { position: absolute; inset: 0; width: 100%; height: 100%; }
  .letterhead .wordmark { position: absolute; left: 18px; top: 14px; }
  .letterhead__body {
    position: absolute; left: 26px; right: 26px; top: 112px;
    font-size: 8.4px; line-height: 10.4px; font-weight: 500;
    text-align: justify; color: var(--ink);
  }
  .letterhead__body p { text-indent: 10px; margin-bottom: 10px; }
  .signature {
    position: absolute; width: 70px; height: 36px;
    background: linear-gradient(90deg, #e4e4e4, #f4f4f4);
  }
  .signature-line { position: absolute; height: 1px; background: var(--muted); width: 120px; }

  /* business cards */
  .card { position: absolute; overflow: hidden; }
  .card--front {
    left: 122px; top: 226px; width: 362px; height: 258px; background: #fff;
    box-shadow: 0 0 0 1px #e3e3e3, 0 3px 8px rgba(0,0,0,.18);
  }
  .card--front .wordmark { position: absolute; left: 16px; top: 16px; }
  .card__name { position: absolute; left: 156px; top: 80px; font-size: 27px; color: var(--brown); font-weight: 400; letter-spacing: .5px; }
  .card__title { position: absolute; left: 234px; top: 112px; font-size: 14px; color: var(--blue); font-weight: 500; }
  .card__contacts { position: absolute; left: 16px; top: 114px; list-style: none; font-size: 7px; color: #333; }
  .card__contacts li { display: flex; align-items: center; gap: 7px; height: 18px; }
  .card__contacts svg { width: 9px; height: 9px; flex: none; fill: var(--blue-dark); }
  .card__contacts li.is-address { height: 24px; line-height: 9px; }
  .card__art { position: absolute; inset: 0; }

  .card--back {
    left: 638px; width: 400px; height: 210px;
    display: flex; flex-direction: column; align-items: center; justify-content: center;
    box-shadow: 0 3px 8px rgba(0,0,0,.25);
  }
  .card--back-blue { top: 100px; background: var(--blue); }
  .card--back-brown { top: 400px; background: var(--brown); }
  .card__web { position: absolute; bottom: 16px; font-size: 8px; color: #fff; font-weight: 500; }
</style>
</head>
<body>

  <section class="panel panel--logo">
    <div class="wordmark wordmark--hero">
      <span class="wordmark__dot"></span>
      <span class="wordmark__name">PT. Bumi Sentosa Abadi</span>
    </div>
  </section>

  <section class="brand-band">
    <div class="wordmark wordmark--band">
      <span class="wordmark__dot"></span>
      <span class="wordmark__name">PT. Bumi Sentosa Abadi</span>
    </div>
  </section>

  <section class="panel panel--letterheads">
    <article class="letterhead letterhead--left">
      <div class="letterhead__paper">
        <svg class="letterhead__art" viewBox="0 0 416 542" preserveAspectRatio="none">
          <polygon points="250,70 416,70 416,78 242,78" fill="var(--brown)"/>
          <polygon points="0,80 416,80 416,84 0,84" fill="var(--blue)"/>
          <polygon points="0,80 124,80 114,92 0,92" fill="var(--blue)"/>
          <path d="M0 470 C 150 460 330 420 416 330 L416 360 C 330 450 160 480 0 490 Z" fill="#f1f1f1"/>
          <path d="M0 505 C 160 495 330 465 416 385 L416 425 C 340 490 180 512 0 522 Z" fill="var(--blue)"/>
          <path d="M0 522 C 180 512 340 490 416 425 L416 542 L0 542 Z" fill="#fff"/>
          <path d="M0 528 C 180 522 340 510 416 480 L416 542 L0 542 Z" fill="var(--brown)"/>
        </svg>
        <div class="wordmark wordmark--small">
          <span class="wordmark__dot"></span>
          <span class="wordmark__name">PT. Bumi Sentosa Abadi</span>
        </div>
        <div class="letterhead__body">
          <p>Lorem ipsum dolor sit amet, consectetuer adipiscing elit. Aenean commodo ligula eget dolor. Aenean massa. Cum sociis natoque penatibus et magnis dis parturient montes, nascetur ridiculus mus. Donec quam felis, ultricies nec, pellentesque eu, pretium quis, sem. Nulla consequat massa quis enim. Donec pede justo, fringilla vel, aliquet nec, vulputate eget, arcu. In enim justo, rhoncus ut, imperdiet a, venenatis vitae, justo. Nullam dictum felis eu pede mollis pretium. Integer tincidunt. Cras dapibus. Vivamus elementum semper nisi. Aenean vulputate eleifend tellus. Aenean leo ligula, porttitor eu, consequat vitae, eleifend ac, enim. Aliquam lorem ante, dapibus in, viverra quis, feugiat a, tellus.</p>
          <p>Lorem ipsum dolor sit amet, consectetuer adipiscing elit. Aenean commodo ligula eget dolor. Aenean massa. Cum sociis natoque penatibus et magnis dis parturient montes, nascetur ridiculus mus. Donec quam felis, ultricies nec, pellentesque eu, pretium quis, sem. Nulla consequat massa quis enim. Donec pede justo, fringilla vel, aliquet nec, vulputate eget, arcu. In enim justo, rhoncus ut, imperdiet a, venenatis vitae, justo. Nullam dictum felis eu pede mollis pretium. Integer tincidunt. Cras dapibus. Vivamus elementum semper nisi.</p>
        </div>
        <div class="signature" role="img" aria-label="Handwritten signature" style="left:62px; top:408px;"></div>
        <div class="signature-line" style="left:40px; top:450px;"></div>
      </div>
    </article>

    <article class="letterhead letterhead--right">
      <div class="letterhead__paper">
        <svg class="letterhead__art" viewBox="0 0 410 542" preserveAspectRatio="none">
          <polygon points="0,60 410,60 410,63 0,63" fill="var(--brown)"/>
          <polygon points="0,58 130,58 122,68 0,68" fill="var(--brown)"/>
          <polygon points="232,66 410,66 410,74 224,74" fill="var(--blue)"/>
          <polygon points="0,518 200,518 192,530 0,530" fill="var(--brown)"/>
          <polygon points="206,518 410,518 410,530 198,530" fill="var(--blue)"/>
        </svg>
        <div class="wordmark wordmark--small">
          <span class="wordmark__dot"></span>
          <span class="wordmark__name">PT. Bumi Sentosa Abadi</span>
        </div>
        <div class="letterhead__body" style="top:100px;">
          <p>Lorem ipsum dolor sit amet, consectetuer adipiscing elit. Aenean commodo ligula eget dolor. Aenean massa. Cum sociis natoque penatibus et magnis dis parturient montes, nascetur ridiculus mus. Donec quam felis, ultricies nec, pellentesque eu, pretium quis, sem. Nulla consequat massa quis enim. Donec pede justo, fringilla vel, aliquet nec, vulputate eget, arcu. In enim justo, rhoncus ut, imperdiet a, venenatis vitae, justo. Nullam dictum felis eu pede mollis pretium. Integer tincidunt. Cras dapibus. Vivamus elementum semper nisi. Aenean vulputate eleifend tellus. Aenean leo ligula, porttitor eu, consequat vitae, eleifend ac, enim. Aliquam lorem ante, dapibus in, viverra quis, feugiat a, tellus.</p>
          <p>Lorem ipsum dolor sit amet, consectetuer adipiscing elit. Aenean commodo ligula eget dolor. Aenean massa. Cum sociis natoque penatibus et magnis dis parturient montes, nascetur ridiculus mus. Donec quam felis, ultricies nec, pellentesque eu, pretium quis, sem. Nulla consequat massa quis enim. Donec pede justo, fringilla vel, aliquet nec, vulputate eget, arcu. In enim justo, rhoncus ut, imperdiet a, venenatis vitae, justo. Nullam dictum felis eu pede mollis pretium. Integer tincidunt. Cras dapibus. Vivamus elementum semper nisi.</p>
        </div>
        <div class="signature" role="img" aria-label="Handwritten signature" style="left:262px; top:406px;"></div>
        <div class="signature-line" style="left:244px; top:448px; width:140px;"></div>
      </div>
    </article>
  </section>

  <section class="panel panel--cards">
    <article class="card card--front">
      <svg class="card__art" viewBox="0 0 362 258" preserveAspectRatio="none">
        <path d="M140 258 C 240 240 320 200 362 140 L362 160 C 320 215 250 245 170 258 Z" fill="#eeeeee"/>
        <path d="M180 258 C 270 240 330 205 362 170 L362 240 C 340 250 310 256 280 258 Z" fill="var(--blue)"/>
        <path d="M280 258 C 310 256 340 250 362 240 L362 258 Z" fill="var(--brown)"/>
      </svg>
      <div class="wordmark wordmark--small">
        <span class="wordmark__dot"></span>
        <span class="wordmark__name">PT. Bumi Sentosa Abadi</span>
      </div>
      <div class="card__name">YOURNAME</div>
      <div class="card__title">yourtitle</div>
      <ul class="card__contacts">
        <li><svg viewBox="0 0 10 10"><path d="M2 0.5 L4 2.5 L3 4 C3.6 5.4 4.6 6.4 6 7 L7.5 6 L9.5 8 L8 9.5 C4 9.2 0.8 6 0.5 2 Z"/></svg>1234567890</li>
        <li><svg viewBox="0 0 10 10"><path d="M0.5 2 H9.5 V8 H0.5 Z M1.2 2.6 L5 5.4 L8.8 2.6" fill="none" stroke="var(--blue-dark)" stroke-width="1"/></svg>your@email.com</li>
        <li><svg viewBox="0 0 10 10"><path d="M1 0.5 H7 L9 2.5 V9.5 H1 Z M3 4 H7 M3 6 H7" fill="none" stroke="var(--blue-dark)" stroke-width="1"/></svg>1234567890</li>
        <li class="is-address"><svg viewBox="0 0 10 10"><path d="M5 0.5 C2.5 0.5 1.5 2.3 1.5 3.8 C1.5 6 5 9.5 5 9.5 C5 9.5 8.5 6 8.5 3.8 C8.5 2.3 7.5 0.5 5 0.5 Z M5 2.5 A1.3 1.3 0 1 0 5 5.1 A1.3 1.3 0 1 0 5 2.5 Z" fill-rule="evenodd"/></svg>your address here your<br>address here</li>
      </ul>
    </article>

    <article class="card card--back card--back-blue">
      <div class="wordmark wordmark--card-back">
        <span class="wordmark__dot"></span>
        <span class="wordmark__name">PT. Bumi Sentosa Abadi</span>
      </div>
      <span class="card__web">www.yoursite.com</span>
    </article>

    <article class="card card--back card--back-brown">
      <div class="wordmark wordmark--card-back">
        <span class="wordmark__dot"></span>
        <span class="wordmark__name">PT. Bumi Sentosa Abadi</span>
      </div>
      <span class="card__web">www.yoursite.com</span>
    </article>
  </section>

</body>
</html>
```